Norwegian Mobile Home/Cabin Producer Needs Brochure Design

We make and deliver our own brand of mobile homes especially made for Norway and it's weather conditions. We differ from other brands in building quality in regards to a much more solid construction, insulation and choices. We work with our customer from the beginning and build them after their demands and wishes.
We need a brochure that holds us out as top of the line. We deliver mobile homes of all kinds and sizes. Both to the private and professional sector.
For the professional sector, mainly camping sites we want to show, lodges-, sanitary- and kitchen wagoons etc.
So we need a brochure of 14-20 pages in A4 where the double pages can be printed in A3 format.
We have logo (provided). But we need cover as well as back suggestions.
It should start with pages where we can teel who we are and stand for.Piicture(s) and space for some editable text (which we can write in norwegian). The text part can have a transparent background......or not. Give us your best shot. Also a smaller part in the private sector that shows winter time.
We want other pages for the private sector that shows what we deliver and the possibilities of choices.
Pages for the the professional sector.
Pages that show our production. How we transport. And the split construction. Only pictures from this portfolio here. (see fotoskap portfolios)
Take a look at provided pictures and our website www.solvikhytta.no for inspiration.
Here's a FotoSkap link to Pictures to choose from. http://bildelagr.example/K4TQ9P
(Hope it Works, let me know if not)
Our company name in small letters "fjordgrønn hyttebygg" means directly translated "fjordgreen cabin builds".
Looking forward to your suggestions.
Target Market(s)
Private market for vacation mobile homes. Camping sites and similar
Industry/Entity Type
Insulation
Requirements
Must have
- Our logo on the front page. Simple but inviting and professional
Logo and address on the back.

```html
<!DOCTYPE html>
<html lang="en">
<head>
<meta charset="utf-8">
<title>fjordgrønn hyttebygg – brochure pages</title>
<link rel="stylesheet" href="https://fonts.googleapis.com/css2?family=Archivo+Black&family=Arimo:wght@400;700&family=Cormorant+Garamond:wght@400&display=swap">
<style>
:root{
  --stage:#55585b;
  --paper:#ffffff;
  --blue:#7f9fd0;
  --blue-deep:#5f82be;
  --blue-pale:#c9d6ee;
  --ink:#555b63;
  --ink-soft:#8a9099;
}
*{box-sizing:border-box;margin:0;padding:0}
html,body{width:1200px;height:900px;overflow:hidden}
body{background:var(--stage);position:relative;font-family:"Arimo",Arial,sans-serif;color:var(--ink)}
.sheet{position:absolute;background:var(--paper);box-shadow:0 4px 14px rgba(0,0,0,.35)}
.cover,.back-cover{width:180px;height:255px}
.spread{width:360px;height:255px;display:flex}
.page{position:relative;width:50%;height:100%;overflow:hidden}
.page.left{border-right:1px solid #e2e2e2}
.photo{position:absolute}
.ph-garden{background:linear-gradient(160deg,#4d6b3f,#7e9b5e 55%,#3c4a35)}
.ph-redcabin{background:linear-gradient(170deg,#557048,#9a3b33 55%,#6e8a4c)}
.ph-interior{background:linear-gradient(150deg,#e9e2d6,#b8a791 60%,#7d6b58)}
.ph-wood{background:linear-gradient(180deg,#5e7d3e,#8a5a38 50%,#6b3f26)}
.ph-white{background:linear-gradient(170deg,#cfd6dc,#f4f4f2 55%,#7a8a6e)}
.ph-factory{background:linear-gradient(180deg,#7d858c,#b9bdc0 50%,#5a6065)}
.ph-kitchen{background:linear-gradient(160deg,#eef0ee,#a9b3a4 55%,#6d6258)}
.ph-terrace{background:linear-gradient(150deg,#d9dcd6,#8fa28a 55%,#3f5a66)}
.ph-truck{background:linear-gradient(170deg,#6e8c5a,#c9b04a 55%,#5d6b4c)}
.ph-plan{background:linear-gradient(180deg,#f4f5f7,#dfe3ea)}
.ph-sky{background:radial-gradient(ellipse at 50% 40%,#dbe8f6,#7eaee0 55%,#3f7cc8)}
.tab{position:absolute;top:3%;right:4%;width:38%;height:4.5%;background:var(--blue);color:#fff;font-size:4px;font-weight:700;letter-spacing:.3px;display:flex;align-items:center;justify-content:center}
.headline{position:absolute;font-family:"Archivo Black",Arial,sans-serif;color:var(--blue);text-transform:uppercase;line-height:1;letter-spacing:.2px}
.intro{position:absolute;font-size:4.6px;line-height:1.3;color:var(--ink-soft)}
.col{position:absolute;font-size:3.4px;line-height:1.4;color:var(--ink)}
.box{position:absolute;background:var(--blue-pale);padding:2px;font-size:3.4px;line-height:1.4;color:var(--ink)}
.box.solid{background:var(--blue);color:#fff}
.caption{position:absolute;height:6%;background:var(--blue);color:#fff;font-size:3.6px;display:flex;align-items:center;justify-content:center}
.quote{position:absolute;font-family:"Cormorant Garamond",Georgia,serif;font-variant:small-caps;color:var(--blue-deep);font-size:8px;line-height:1.05}
.label{position:absolute;font-size:4px;font-weight:700;color:var(--blue-deep);text-transform:uppercase}
.brand{position:absolute;display:flex;align-items:center;gap:4px;font-family:"Arimo",Arial,sans-serif;font-weight:700;text-transform:uppercase;letter-spacing:.6px}
.brand-mark{width:6px;height:6px;flex:none}
.cover .brand{top:10px;left:12px;font-size:8px;color:var(--ink)}
.cover .brand-mark{background:var(--ink)}
.back-cover .brand{top:170px;left:22px;font-size:8px;color:#fff}
.back-cover .brand-mark{background:#fff}
.back-cover .address{position:absolute;bottom:8px;left:0;right:0;text-align:center;font-size:5px;line-height:1.5;color:var(--blue-deep);letter-spacing:.3px}
</style>
</head>
<body>

<!-- front cover -->
<section class="sheet cover" style="left:105px;top:30px">
  <div class="brand"><span class="brand-mark"></span>fjordgrønn hyttebygg</div>
  <div class="photo ph-garden" role="img" aria-label="Grey cabin with white railing among pine trees" style="left:12px;top:32px;width:156px;height:210px"></div>
</section>

<!-- spread: about us -->
<section class="sheet spread" style="left:330px;top:30px">
  <div class="page left">
    <div class="photo ph-redcabin" role="img" aria-label="Red and white cabins on a lawn among trees" style="left:0;top:0;width:100%;height:32%"></div>
    <div class="photo ph-interior" role="img" aria-label="Bright cabin living room" style="left:0;top:33%;width:100%;height:28%"></div>
    <div class="box" style="left:45%;top:37%;width:40%;height:20%;background:#fff;border:1px solid var(--blue-pale)">Built for Norwegian weather.</div>
    <div class="photo ph-wood" role="img" aria-label="Wooden deck with bench and lawn" style="left:0;top:62%;width:100%;height:18%"></div>
    <div class="photo ph-redcabin" role="img" aria-label="Red cabin with white fence" style="left:0;top:81%;width:100%;height:19%"></div>
  </div>
  <div class="page right">
    <div class="tab">ABOUT US</div>
    <div class="photo ph-white" role="img" aria-label="White mobile home with wide windows" style="left:4%;top:9%;width:92%;height:28%"></div>
    <div class="quote" style="left:5%;top:40%;width:58%">We have the Dreams,<br>we know the possibilities!</div>
    <div class="col" style="left:5%;top:53%;width:55%">Every cabin is built to order with solid walls, thick insulation and a layout chosen with you.</div>
    <div class="col" style="left:66%;top:42%;width:30%">Every cabin is built to order with solid walls, thick insulation and a layout chosen with you.</div>
    <div class="photo ph-interior" role="img" aria-label="Cabin living room with sofa" style="left:4%;top:66%;width:44%;height:24%"></div>
    <div class="caption" style="left:4%;top:90%;width:44%">PROJECT NAME</div>
    <div class="photo ph-kitchen" role="img" aria-label="Cabin lounge with purple accents" style="left:52%;top:66%;width:44%;height:24%"></div>
    <div class="caption" style="left:52%;top:90%;width:44%">PROJECT NAME</div>
  </div>
</section>

<!-- spread: pro sector -->
<section class="sheet spread" style="left:735px;top:30px">
  <div class="page left">
    <div class="photo ph-garden" role="img" aria-label="White lodge with red door on a green slope" style="left:0;top:0;width:100%;height:50%"></div>
    <div class="headline" style="left:5%;top:54%;width:90%;font-size:10px">I'm the titel for<br>pro sector!!!</div>
    <div class="box" style="left:5%;top:70%;width:30%;height:22%">Every cabin is built to order with solid walls, thick insulation and a layout chosen with you.</div>
    <div class="col" style="left:39%;top:70%;width:27%">Every cabin is built to order with solid walls, thick insulation and a layout chosen with you.</div>
    <div class="col" style="left:69%;top:70%;width:27%">Every cabin is built to order with solid walls, thick insulation and a layout chosen with you.</div>
  </div>
  <div class="page right">
    <div class="tab" style="top:1%">PRO SECTOR</div>
    <div class="photo ph-factory" role="img" aria-label="Mobile homes inside production hall" style="left:4%;top:7%;width:92%;height:20%"></div>
    <div class="photo ph-interior" role="img" aria-label="Warm lit lodge interior" style="left:38%;top:28%;width:58%;height:22%"></div>
    <div class="col" style="left:4%;top:30%;width:31%">Every cabin is built to order with solid walls, thick insulation and a layout chosen with you.</div>
    <div class="photo ph-plan" role="img" aria-label="Floor plan of a lodge unit" style="left:38%;top:52%;width:58%;height:16%;border:1px solid var(--blue-pale)"></div>
    <div class="box solid" style="left:4%;top:74%;width:92%;height:12%">Every cabin is built to order with solid walls, thick insulation and a layout chosen with you.</div>
  </div>
</section>

<!-- spread: private sector -->
<section class="sheet spread" style="left:105px;top:322px">
  <div class="page left">
    <div class="photo ph-terrace" role="img" aria-label="Terrace with garden table and flowers" style="left:0;top:0;width:100%;height:50%"></div>
    <div class="headline" style="left:0;right:0;top:53%;text-align:center;font-size:11px">I am the titel!!!</div>
    <div class="intro" style="left:8%;top:61%;width:84%">Ibusaniam, qui alitaque osto volum intur am qui cusa non corature ceaturemque pos dit hillenimus et adipid qui ne</div>
    <div class="photo ph-interior" role="img" aria-label="Wicker chair with cushions by the window" style="left:4%;top:74%;width:26%;height:22%"></div>
    <div class="col" style="left:34%;top:74%;width:30%">Every cabin is built to order with solid walls, thick insulation and a layout chosen with you.</div>
    <div class="col" style="left:67%;top:74%;width:29%">Every cabin is built to order with solid walls, thick insulation and a layout chosen with you.</div>
  </div>
  <div class="page right">
    <div class="tab">PRIVATE SECTOR</div>
    <div class="photo ph-kitchen" role="img" aria-label="Kitchen sink with herbs on the counter" style="left:4%;top:9%;width:92%;height:28%"></div>
    <div class="photo ph-interior" role="img" aria-label="Bright living room with green cushions" style="left:4%;top:38%;width:92%;height:25%"></div>
    <div class="caption" style="left:4%;top:63%;width:92%">Built for Norwegian weather.</div>
    <div class="photo ph-redcabin" role="img" aria-label="Dark cabin with red deck chairs" style="left:4%;top:72%;width:40%;height:24%"></div>
    <div class="label" style="left:50%;top:72%">Technical info</div>
    <div class="col" style="left:50%;top:77%;width:46%">Every cabin is built to order with solid walls, thick insulation and a layout chosen with you.</div>
  </div>
</section>

<!-- spread: production and construction -->
<section class="sheet spread" style="left:510px;top:322px">
  <div class="page left">
    <div class="photo ph-white" role="img" aria-label="White mobile home at dusk" style="left:0;top:0;width:100%;height:30%"></div>
    <div class="headline" style="left:4%;top:33%;width:52%;font-size:8.5px">Production &amp;<br>transport!</div>
    <div class="intro" style="left:58%;top:33%;width:38%;font-size:3.8px">Ibusaniam, qui alitaque osto volum intur</div>
    <div class="box" style="left:4%;top:45%;width:30%;height:25%">Every cabin is built to order with solid walls, thick insulation and a layout chosen with you.</div>
    <div class="photo ph-factory" role="img" aria-label="Production line with blue rails" style="left:37%;top:45%;width:59%;height:25%"></div>
    <div class="photo ph-truck" role="img" aria-label="Truck carrying a mobile home" style="left:4%;top:73%;width:55%;height:24%"></div>
  </div>
  <div class="page right">
    <div class="photo ph-factory" role="img" aria-label="Mobile home section in the production hall" style="left:4%;top:3%;width:92%;height:27%"></div>
    <div class="headline" style="left:12%;top:33%;width:84%;text-align:center;font-size:8.5px">Titel for<br>construction!</div>
    <div class="photo ph-plan" role="img" aria-label="Split construction drawing of a mobile home" style="left:4%;top:46%;width:30%;height:48%"></div>
    <div class="photo ph-plan" role="img" aria-label="Section drawing of the cabin module" style="left:38%;top:46%;width:58%;height:18%;border:1px solid var(--blue-pale)"></div>
    <div class="box solid" style="left:38%;top:67%;width:58%;height:27%">Every cabin is built to order with solid walls, thick insulation and a layout chosen with you.<br>Every cabin is built to order with solid walls, thick insulation and a layout chosen with you.</div>
  </div>
</section>

<!-- back cover -->
<section class="sheet back-cover" style="left:915px;top:322px">
  <div class="photo ph-sky" role="img" aria-label="Blue sky with a heart drawn in cloud" style="left:10px;top:10px;width:160px;height:200px"></div>
  <div class="brand"><span class="brand-mark"></span>fjordgrønn hyttebygg</div>
  <div class="address">FJORDGRØNN HYTTEBYGG AS<br>POSTBOKS 12 • 6120 FJORDVIK<br>PHONE 40 00 12 34 • WWW.SOLVIKHYTTA.NO</div>
</section>

<!-- spread: private cabins -->
<section class="sheet spread" style="left:420px;top:614px">
  <div class="page left">
    <div class="photo ph-garden" role="img" aria-label="Grey cabin with white railing and lawn" style="left:0;top:0;width:100%;height:48%"></div>
    <div class="photo ph-redcabin" role="img" aria-label="Red cabin in winter" style="left:4%;top:50%;width:40%;height:16%"></div>
    <div class="photo ph-interior" role="img" aria-label="Living room with green cushions" style="left:48%;top:50%;width:48%;height:16%"></div>
    <div class="label" style="left:4%;top:69%">Technical info</div>
    <div class="col" style="left:4%;top:74%;width:40%">Every cabin is built to order with solid walls, thick insulation and a layout chosen with you.</div>
    <div class="photo ph-kitchen" role="img" aria-label="White bathroom with blue mat" style="left:48%;top:68%;width:48%;height:16%"></div>
    <div class="col" style="left:48%;top:86%;width:48%">Every cabin is built to order with solid walls, thick insulation and a layout chosen with you.</div>
  </div>
  <div class="page right">
    <div class="tab">PRIVATE SECTOR</div>
    <div class="headline" style="left:5%;top:10%;width:90%;font-size:11px">I am the titel!!!</div>
    <div class="intro" style="left:5%;top:17%;width:90%">Ibusaniam, qui alitaque osto volum intur am qui cusa non corature ceaturemque pos dit hillenimus et adipid qui ne</div>
    <div class="photo ph-interior" role="img" aria-label="Cabin lounge with sofa and windows" style="left:5%;top:30%;width:91%;height:28%"></div>
    <div class="photo ph-kitchen" role="img" aria-label="Kitchen sink with plant" style="left:5%;top:60%;width:60%;height:34%"></div>
    <div class="col" style="left:69%;top:62%;width:27%">Every cabin is built to order with solid walls, thick insulation and a layout chosen with you.</div>
  </div>
</section>

</body>
</html>
```